Help develop the "Breezy Brew" Logo & Can Design for new beer!

We're a new beer being produced in the Caribbean. Thus looking for a beer logo design that
1) capitalizes on the word "Breezy" for further beer lines that spin off of this first one. EXAMPLES OF OTHER BEER NAMES TO BE PRODUCED THAT HAVE TO HAVE TIE IN TO ORIGINAL DESIGN: "One Breezy Brew", "Sunny Pelican Wobble Brew" "Ramblefoot Breezy Brew" "Wharrya doin' Breezy Brew" "Bout now for Breezy Brew", "Tamarna Breezy Brew" etc etc etc,

2) has unique visual impact,
3) Logo has to be usable across variety of mediums,
4) 4 color maximum,
5) Island art feel,
6) Breezy Brew needs to convey a since of "lightness and slight tongue-in-cheek or off beat humor"...but not overwhelming,
7) Each subsequent label names (see above) needs to be distinctly color coded, but connects to the overarching theme of the brand with distinctive interpretations of each beer’s name.
8) Needs to be BOLD in statement and color.

You can get inspiration from some of these logo's. Follow this link: http://www.quorvelstudio.com/vintage-logos/
or http://www.tindralcrate.com/2014/12/30-beers-for-30-years-2001-to-2006.html

Also see attached files for inspiration!!!

Reason: We've extended the deadline for this project! Thus submit any new designs sooner than later. Thanks!

Target Market(s)

Male: Wear jeans & baseball cap, Played H.S. sports, Hunts/fish/golfDrive a truck or SUV, Work a blue collar job, Like working in the garage or on the landLike football/basketball/baseball, Are married high school sweetheart and have childrenAre from southern states...or wished they were, Chews tobacco or smokeDrink beerFemale: Attended college/community collegeAre married with kidsRide motorcycles, 4x4, ATV’sDrive Trucks or vansFish/camp/garden/sewDo craftsDrink beerGets manicures/pedicuresWears jewelry & jeans

Logo Text

Breezy Brew

Logo styles of interest
Emblem Logo
Pictorial/Combination Logo
Abstract Logo
Character Logo
Wordmark Logo
Requirements
Must have
• Eye catching & readable shelf presentation. Non-Standard art. High definition. Bold Statement. Clear design elements, various color options, High color contrast (like attached files) are needed for visual impact. Simple elements that conveys essence of the brand.
• You are designing the whole "beer can" logo elements, not just the the main logo. Things like background and side panels. Back panel for ingredients and messages to be added to. This is an "overall" can design, not just a single logo design.
• MUST HAVE THESE WORDS/SENTENCES/SECTIONS:
• Sentences: Our Breezy ales and lagers are handcrafted with some of the best ingredients the Caribbean has to offer!
• Section: So, Why Do we use can's?
• Can's eliminate potential light damage, reduce the risk of oxidation are lighter and chill quicker. Can be enjoyed on beaches and make for great recycling and table art. Plus they are the most recycled and eco-friendly material we can use. Breezy!
• BREWED AND BOTTLED/PACKED BY:
• IMPORTED BY
• ALCOHOL (ALC) ______% BY VOLUME (VOL)
• Recyclable
• GOVERNMENT WARNING:
• (1) According to the Surgeon General, women should not drink alcoholic beverages during pregnancy because of the risk of birth defects. (2) Consumption of
• alcoholic beverages impairs your ability to drive a car or operate machinery, and may cause health problems.
• Description: (This will change from beer to beer but this is good example of type language we would be using. "This Breezy Brew has a pletheria of Island goodness (there are hints of passion fruit, mango, and pineapple) along with some pleasant bitterness IPAs are known for. We can honestly say these sweet and savory flavors pair perfectly with this beer and you'll get a kick out of the IPA notes too!"
Should not have
• nudity, graphic language, skulls, flames,

```html
<!DOCTYPE html>
<html lang="en">
<head>
<meta charset="utf-8">
<title>Breezy Brew – Can Labels</title>
<link rel="stylesheet" href="https://fonts.googleapis.com/css2?family=Cinzel:wght@700&family=Libre+Baskerville:wght@700&display=swap">
<style>
  :root {
    --can-red: #c4343b;
    --can-red-dark: #a82a31;
    --label-silver: #e4e5e7;
    --label-silver-light: #f6f6f7;
    --brand-navy: #1c2a4a;
    --tagline-olive: #7d7440;
    --page-white: #ffffff;
  }
  html, body {
    margin: 0;
    padding: 0;
    width: 1200px;
    height: 1186px;
    overflow: hidden;
    background: var(--page-white);
  }
  .canvas {
    position: relative;
    width: 1200px;
    height: 1186px;
  }
  .can-label {
    position: absolute;
    display: flex;
    flex-direction: column;
  }
  .can-label--standard { left: 105px; top: 290px; width: 400px; height: 735px; }
  .can-label--tall { left: 628px; top: 72px; width: 430px; height: 975px; }

  .band--red {
    background: linear-gradient(90deg, var(--can-red-dark), var(--can-red) 30%, var(--can-red) 70%, var(--can-red-dark));
  }
  .band--silver {
    background: linear-gradient(90deg, var(--label-silver), var(--label-silver-light) 35%, var(--label-silver-light) 65%, var(--label-silver));
    display: flex;
    flex-direction: column;
    align-items: center;
    justify-content: center;
    text-align: center;
  }
  .can-label--standard .band--top { height: 150px; }
  .can-label--standard .band--silver { height: 398px; }
  .can-label--standard .band--bottom { flex: 1; }
  .can-label--tall .band--top { height: 235px; }
  .can-label--tall .band--silver { height: 375px; }
  .can-label--tall .band--bottom { flex: 1; }

  .brand-name {
    margin: 0;
    font-family: "Cinzel", serif;
    font-weight: 700;
    color: var(--brand-navy);
    line-height: 1.05;
  }
  .can-label--standard .brand-name { font-size: 66px; }
  .can-label--tall .brand-name { font-size: 70px; }

  .tagline {
    margin: 18px 0 0;
    font-family: "Libre Baskerville", serif;
    font-weight: 700;
    font-size: 10px;
    color: var(--tagline-olive);
    max-width: 300px;
    line-height: 1.4;
  }
</style>
</head>
<body>
<main class="canvas">
  <section class="can-label can-label--standard" aria-label="Breezy Brew standard can label">
    <div class="band band--red band--top"></div>
    <div class="band band--silver">
      <h1 class="brand-name">Breezy<br>Brew</h1>
      <p class="tagline">Our Breezy ales and lagers are handcrafted with some of the best ingredients the Caribbean has to offer!</p>
    </div>
    <div class="band band--red band--bottom"></div>
  </section>

  <section class="can-label can-label--tall" aria-label="Breezy Brew tall can label">
    <div class="band band--red band--top"></div>
    <div class="band band--silver">
      <h2 class="brand-name">Breezy<br>Brew</h2>
      <p class="tagline">Our Breezy ales and lagers are handcrafted with some of the best ingredients the Caribbean has to offer!</p>
    </div>
    <div class="band band--red band--bottom"></div>
  </section>
</main>
</body>
</html>
```